Mobile Oil Change company needs a flyer to promote new business

We need a flyer to 1) print & handout and 2) email out to potential customers. We are a mobile oil change company that comes to our customer locations to perform the work instead of customers going to traditional oil change companies. We have a 21 point inspection with our oil change. (21 point inspection details will not be on the flyer). Would like to keep the flyer simple but creative. I'm attaching 1) the write-up we created, 2) our logo (logo color is dark teal on white but other combinations are included if you wanted to propose a different color combination), and 3) additional services we offer. Logo font is Alegreya Sans.
Would like the additional services listed with icons and brief descriptions (similar to attachment) without pricing. Company website for reference is www.brindlefleetcare.com.

Target Market(s)

Companies with many service vehicles such as Oil & Gas service companies, heating and air conditioning companies, utility companies, police departments, etc. Companies that prioritize convenience and maintenance first.

Font styles to use
Sans Serif

Colors
00a990

Requirements
Must have
• Simple but creative design with our logo at top of the flyer. Additional Services (details in document supplied) can be smaller and less prominent than other "main" content listed in the CONTENT document supplied.
Should not have
• Do not use animated character graphics in the flyer and limit (1) stock photos to A small area in the flyer.

```html
<!DOCTYPE html>
<html lang="en">
<head>
<meta charset="utf-8">
<title>Brindle Fleet Care – Mobile Oil Change Flyer</title>
<link rel="stylesheet" href="https://fonts.googleapis.com/css2?family=Anton&family=Montserrat:wght@700;800;900&family=Lato:wght@400;700&display=swap">
<style>
  :root {
    --teal: #00a990;
    --black: #050505;
    --white: #ffffff;
    --page: #2c3446;
    --photo-warm: rgba(120, 88, 24, .38);
    --photo-cool: rgba(48, 48, 48, .45);
  }
  * { box-sizing: border-box; margin: 0; padding: 0; }
  html, body { width: 1200px; height: 1200px; overflow: hidden; background: var(--page); }
  .flyer {
    position: absolute; left: 170px; top: 44px;
    width: 860px; height: 1112px;
    background: var(--white); overflow: hidden;
    font-family: "Lato", sans-serif;
  }
  .flyer__backdrop { position: absolute; inset: 0; }
  .flyer__photo {
    position: absolute; right: 0; top: 0; width: 460px; height: 600px;
    background: linear-gradient(180deg, var(--photo-warm) 0%, var(--photo-cool) 55%, rgba(5,5,5,0) 100%);
  }
  .logo {
    position: absolute; left: 40px; top: 96px; width: 370px; height: 110px;
    border: 3px solid var(--teal); border-radius: 0 26px 0 0;
    display: flex; align-items: center; justify-content: center; gap: 12px;
  }
  .logo__mark { width: 14px; height: 14px; background: var(--teal); flex: none; }
  .logo__name {
    font-family: "Montserrat", sans-serif; font-weight: 800; font-size: 25px;
    color: var(--teal); letter-spacing: 1px; white-space: nowrap;
  }
  .headline { position: absolute; left: 40px; top: 230px; }
  .headline__big {
    font-family: "Anton", sans-serif; font-size: 104px; line-height: 1;
    color: var(--teal); letter-spacing: 1px;
  }
  .headline__line {
    font-family: "Montserrat", sans-serif; font-weight: 900; font-size: 44px;
    line-height: 1.05; color: var(--white);
  }
  .headline__line--teal { color: var(--teal); }
  .intro {
    position: absolute; left: 40px; top: 468px; width: 440px;
    font-family: "Montserrat", sans-serif; font-weight: 800; font-size: 22px;
    line-height: 1.25; color: var(--white);
  }
  .steps { position: absolute; left: 40px; top: 570px; list-style: none; width: 470px; }
  .steps__item {
    display: flex; align-items: flex-start; gap: 10px;
    color: var(--white); font-size: 15.5px; line-height: 1.2; margin-bottom: 8px;
  }
  .steps__num {
    flex: none; width: 19px; height: 19px; border-radius: 50% 0 50% 50%;
    transform: rotate(-45deg); background: var(--teal);
    display: flex; align-items: center; justify-content: center;
  }
  .steps__num span { transform: rotate(45deg); font-size: 11px; font-weight: 700; color: var(--white); }
  .benefits {
    position: absolute; left: 250px; top: 745px; width: 580px; height: 180px;
    border: 3px solid var(--teal); border-radius: 26px; background: var(--black);
    display: flex; flex-direction: column; justify-content: center; align-items: center;
    text-align: center; gap: 10px;
    font-family: "Montserrat", sans-serif; font-weight: 700; font-size: 20px; color: var(--white);
  }
  .cta {
    position: absolute; right: 70px; top: 938px;
    font-family: "Anton", sans-serif; font-size: 82px; line-height: 1; color: var(--teal);
  }
  .contacts {
    position: absolute; left: 40px; right: 40px; top: 1055px;
    display: flex; justify-content: space-between; align-items: center;
    font-size: 17px; color: var(--black);
  }
  .contacts__item { display: flex; align-items: center; gap: 7px; }
  .contacts__item--phone { font-family: "Montserrat", sans-serif; font-weight: 800; font-size: 20px; }
  .contacts__icon { width: 18px; height: 18px; flex: none; }
</style>
</head>
<body>
<main class="flyer">
  <svg class="flyer__backdrop" width="860" height="1112" viewBox="0 0 860 1112" aria-hidden="true">
    <path d="M0 0 H860 V560 C850 760 760 820 560 880 L0 1010 Z" fill="#00a990"/>
    <path d="M0 0 H860 V560 C845 730 760 780 560 835 L0 965 Z" fill="#050505"/>
  </svg>
  <div class="flyer__photo" role="img" aria-label="Photo of motor oil being poured into a vehicle engine"></div>

  <div class="logo">
    <span class="logo__mark"></span>
    <span class="logo__name">BRINDLE FLEET CARE</span>
  </div>

  <h1 class="headline">
    <div class="headline__big">HASSLE FREE</div>
    <div class="headline__line">OIL CHANGES ON</div>
    <div class="headline__line headline__line--teal">YOUR TERMS</div>
  </h1>

  <p class="intro">Our simple 5-step process lets you schedule an appointment and get service to save time and money:</p>

  <ol class="steps">
    <li class="steps__item"><span class="steps__num"><span>1</span></span>Call or email us to schedule service</li>
    <li class="steps__item"><span class="steps__num"><span>2</span></span>Our highly trained technicians come to you for service</li>
    <li class="steps__item"><span class="steps__num"><span>3</span></span>Service is performed quickly on your vehicle</li>
    <li class="steps__item"><span class="steps__num"><span>4</span></span>Pay agreed-upon pricing and receipt is emailed to you</li>
    <li class="steps__item"><span class="steps__num"><span>5</span></span>Services performed are tracked electronically and reminders created</li>
  </ol>

  <div class="benefits">
    <p>High quality synthetic oil used is best suited for<br>commercial vehicles</p>
    <p>Service includes a 21-point inspection</p>
    <p>Additional services are available</p>
  </div>

  <div class="cta">CALL NOW AT</div>

  <div class="contacts">
    <span class="contacts__item contacts__item--phone">
      <svg class="contacts__icon" viewBox="0 0 24 24"><path fill="#00a990" d="M6.6 10.8a15 15 0 0 0 6.6 6.6l2.2-2.2c.3-.3.7-.4 1-.2 1.1.4 2.3.6 3.6.6.6 0 1 .4 1 1V20c0 .6-.4 1-1 1A17 17 0 0 1 3 4c0-.6.4-1 1-1h3.5c.6 0 1 .4 1 1 0 1.3.2 2.5.6 3.6.1.3 0 .7-.2 1z"/></svg>
      (833) 555-0142
    </span>
    <span class="contacts__item">
      <svg class="contacts__icon" viewBox="0 0 24 24"><rect x="2" y="5" width="20" height="14" fill="#00a990"/><path d="M2 5 L12 13 L22 5" fill="none" stroke="#fff" stroke-width="2"/></svg>
      Sales@BrindleFleetCare.com
    </span>
    <span class="contacts__item">
      <svg class="contacts__icon" viewBox="0 0 24 24"><circle cx="12" cy="12" r="9" fill="none" stroke="#00a990" stroke-width="2"/><path d="M3 12h18M12 3c3 3 3 15 0 18M12 3c-3 3-3 15 0 18" fill="none" stroke="#00a990" stroke-width="1.6"/></svg>
      www.brindlefleetcare.com
    </span>
  </div>
</main>
</body>
</html>
```